Design a Web Development Agency Website

This project is to design a website for a Web Development Agency named Quenvado.
Please design the landing page first and if your design is selected then you can design the Services, About Us, and Portfolio page.
This web agency is targeted to the African market specifically small businesses in Nigeria so the design should be modern, professional, clean and elegant.

The name of the company as shall appear in the footer is Quenvado Communications Ltd.

Industry/Entity Type

Web design, small to med sized business

Number of Pages Required

4 page

Font styles to use
Sans Serif

Colors
00AB8E
00BBA5
67D7C9
C6EFE9
E9F9F6
F0912C
F2A743
F7CA91
FBE8D2
FDF5EE

Requirements
Must have
• Professional, clean home page, MUST deliver in Figma

```html
<!DOCTYPE html>
<html lang="en">
<head>
<meta charset="utf-8">
<title>Quenvado Communications Ltd</title>
<link href="https://fonts.googleapis.com/css2?family=Montserrat:ital,wght@0,400;0,500;0,600;0,700;0,800;1,400;1,500&family=Mulish:ital,wght@0,400;0,600;1,400&display=swap" rel="stylesheet">
<style>
:root{
  --green:#00AB8E;
  --green-2:#00BBA5;
  --green-3:#67D7C9;
  --orange:#F0912C;
  --orange-2:#F2A743;
  --peach:#F7CA91;
  --ink:#2b2b2b;
  --text:#4a4a4a;
  --muted:#6b6b6b;
  --grey-bg:#f1f1f1;
  --footer:#2f2f2f;
  --white:#ffffff;
}
*{margin:0;padding:0;box-sizing:border-box}
html,body{width:1200px;height:4146px;overflow:hidden}
body{position:relative;font-family:'Montserrat',sans-serif;color:var(--text);background:var(--white)}
.abs{position:absolute}
.logo{font-family:'Montserrat',sans-serif;color:var(--ink)}
.logo-name{font-weight:800;font-size:32px;letter-spacing:.5px;line-height:1}
.logo-sub{font-weight:500;font-size:13px;letter-spacing:1px;margin-top:6px}

/* header */
.header{left:0;top:0;width:1200px;height:60px}
.nav{left:346px;top:27px;display:flex;font-size:13.5px;color:var(--ink)}
.nav span{position:absolute;white-space:nowrap}
.nav .active{color:var(--orange)}
.nav .active:after{content:"";position:absolute;left:0;top:24px;width:36px;height:2px;background:var(--orange)}
.call{left:925px;top:0;width:275px;height:60px;background:var(--green);color:#fff}
.call-icon{left:12px;top:14px;width:32px;height:32px;border-radius:50%;background:var(--orange)}
.call-lbl{left:52px;top:12px;font-size:11px}
.call-num{left:52px;top:27px;font-size:16px;font-weight:700}

/* hero */
.hero{left:0;top:0;width:1200px;height:703px;background:linear-gradient(100deg,#d9cfc1 0%,#ece7e0 25%,#f3f1ee 50%,#e8e1d6 75%,#cfc3b3 100%)}
.hero-title{left:0;width:1200px;text-align:center;color:var(--ink);font-weight:800}
.hero-title.t1{top:212px;font-size:68px;letter-spacing:2px}
.hero-title.t2{top:298px;font-size:43px;letter-spacing:1.5px}
.btn{display:flex;align-items:center;justify-content:space-between;height:46px;padding:0 10px 0 20px;background:var(--green);color:#fff;font-weight:700;font-size:13px;letter-spacing:.5px;border-radius:3px;box-shadow:0 4px 10px rgba(0,0,0,.15)}
.btn i{width:28px;height:28px;border-radius:50%;background:#fff;display:flex;align-items:center;justify-content:center}
.hero-arrow{width:60px;height:60px;border-radius:50%;border:1.5px solid rgba(255,255,255,.8);display:flex;align-items:center;justify-content:center}

/* who we are */
.section-title{font-size:38px;font-weight:400;color:var(--ink);letter-spacing:.5px}
.section-title b{color:var(--green);font-weight:700}
.rule{height:4px;background:var(--orange)}
.about-text{left:664px;top:852px;width:422px;font-family:'Mulish',sans-serif;font-size:14.6px;line-height:25.7px;text-align:justify;color:var(--text)}

/* services */
.services{left:0;top:1255px;width:1200px;height:1137px;background:var(--grey-bg)}
.card{width:309px;height:420px;background:#fff;box-shadow:0 4px 14px rgba(0,0,0,.12);text-align:center}
.card .ph{position:absolute;left:8px;top:8px;width:293px;height:278px}
.card h3{position:absolute;left:0;width:100%;top:306px;font-size:19px;font-weight:700;color:var(--green);letter-spacing:.3px}
.card p{position:absolute;left:20px;right:20px;top:340px;font-family:'Mulish',sans-serif;font-size:12.5px;line-height:19px;color:var(--text)}
.card a{position:absolute;left:0;width:100%;top:388px;font-size:13px;font-style:italic;color:var(--muted);text-decoration:underline}

/* testimonials */
.testi{left:0;top:2392px;width:1200px;height:587px;background:radial-gradient(ellipse at 80% 30%,#1cb49c 0%,var(--green) 45%,#079e85 100%)}
.tcard{width:460px;height:254px;background:#fff;text-align:center}
.tcard p{position:absolute;left:28px;right:28px;top:22px;font-size:13.4px;line-height:21.5px;font-style:italic;color:var(--muted)}
.tcard .bar{position:absolute;left:205px;top:174px;width:50px;height:2px;background:var(--green)}
.tcard .name{position:absolute;left:0;width:100%;top:192px;font-size:16px;font-weight:600;color:var(--ink)}
.tcard .role{position:absolute;left:0;width:100%;top:216px;font-size:13px;font-style:italic;color:var(--text)}

/* blog */
.post{background:#fff;padding:20px 10px 14px 16px;overflow:hidden}
.post h4{font-size:15px;font-weight:600;line-height:24px;color:var(--ink);text-transform:uppercase;letter-spacing:.1px}
.post p{font-family:'Mulish',sans-serif;font-size:12px;line-height:19px;color:var(--text);margin-top:6px;padding-right:6px}
.post a{display:inline-flex;align-items:center;gap:10px;margin-top:14px;font-size:15px;line-height:22px;font-style:italic;color:var(--orange);text-decoration:underline}
.post-side{width:318px;box-shadow:0 3px 12px rgba(0,0,0,.12);border-bottom:4px solid var(--orange)}

/* footer */
.footer{left:0;top:3780px;width:1200px;height:366px;background:var(--footer);color:#fff}
.fcol h5{font-size:19px;font-weight:700;letter-spacing:.3px}
.fcol .rule{width:43px;height:3px;margin-top:14px}
.fcol ul{list-style:none;margin-top:14px;font-size:11.5px;font-weight:500;line-height:24px;text-transform:uppercase}
.social{width:32px;height:32px;border-radius:50%;border:1.5px solid #fff}
</style>
</head>
<body>

<!-- hero -->
<div class="abs hero" role="img" aria-label="Photo of a smiling woman working on a laptop at a bright office desk with plants"></div>

<header class="abs header">
  <div class="abs logo" style="left:113px;top:20px">
    <div class="logo-name">QUENVADO</div>
    <div class="logo-sub">COMMUNICATIONS LTD</div>
  </div>
  <nav class="abs nav">
    <span class="active" style="left:0">Home</span>
    <span style="left:75px">Our Services</span>
    <span style="left:198px">About Us</span>
    <span style="left:294px">Testimonials</span>
    <span style="left:412px">Blog</span>
    <span style="left:479px">Contact Us</span>
  </nav>
  <div class="abs call">
    <div class="abs call-icon">
      <svg width="32" height="32" viewBox="0 0 32 32"><path d="M11 9c1 0 2 2.5 2.3 3.5.2.8-1.3 1.6-1.1 2.3.6 1.8 2.3 3.6 4 4.3.7.2 1.5-1.3 2.3-1.1 1 .3 3.5 1.3 3.5 2.300 1.3-1.5 2.8-2.8 2.8C13 23 9 19 9 12c0-1.3 1-3 2-3z" fill="#fff"/></svg>
    </div>
    <div class="abs call-lbl">Call Us</div>
    <div class="abs call-num">+1 (555) 014 2290</div>
  </div>
</header>

<div class="abs hero-title t1">QUENVADO</div>
<div class="abs hero-title t2">COMMUNICATIONS LTD</div>
<div class="abs btn" style="left:515px;top:364px;width:170px">LEARN MORE <i><svg width="14" height="14" viewBox="0 0 14 14"><path d="M2 7h10M8 3l4 4-4 4" stroke="#00AB8E" stroke-width="1.8" fill="none"/></svg></i></div>
<svg class="abs" style="left:44px;top:372px" width="22" height="16" viewBox="0 0 22 16"><path d="M21 8H2M8 2L2 8l6 6" stroke="#F0912C" stroke-width="2" fill="none"/></svg>
<div class="abs hero-arrow" style="left:1115px;top:350px"><svg width="22" height="16" viewBox="0 0 22 16"><path d="M1 8h19M14 2l6 6-6 6" stroke="#F0912C" stroke-width="2" fill="none"/></svg></div>

<!-- who we are -->
<svg class="abs" style="left:0;top:703px" width="480" height="552" viewBox="0 0 480 552"><polygon points="0,0 294,0 478,552 0,552" fill="#F0912C"/></svg>
<div class="abs" style="left:113px;top:788px;width:516px;height:381px;background:linear-gradient(120deg,#c9c4bc,#e6e3de 50%,#9ea5ad)" role="img" aria-label="Photo of two colleagues reviewing work on a computer in an office"></div>
<svg class="abs" style="left:464px;top:1058px" width="200" height="146" viewBox="0 0 200 146">
  <g fill="#F0912C">
    <circle cx="175" cy="4" r="1.6"/><circle cx="195" cy="4" r="1.6"/>
    <circle cx="175" cy="22" r="1.6"/><circle cx="195" cy="22" r="1.6"/>
    <circle cx="175" cy="40" r="1.6"/><circle cx="195" cy="40" r="1.6"/>
    <circle cx="175" cy="58" r="1.6"/><circle cx="195" cy="58" r="1.6"/>
    <circle cx="175" cy="76" r="1.6"/><circle cx="195" cy="76" r="1.6"/>
    <circle cx="175" cy="94" r="1.6"/><circle cx="195" cy="94" r="1.6"/>
    <circle cx="175" cy="112" r="1.6"/><circle cx="195" cy="112" r="1.6"/>
    <circle cx="175" cy="130" r="1.6"/><circle cx="195" cy="130" r="1.6"/>
    <circle cx="4" cy="122" r="1.6"/><circle cx="24" cy="122" r="1.6"/><circle cx="44" cy="122" r="1.6"/><circle cx="64" cy="122" r="1.6"/><circle cx="84" cy="122" r="1.6"/><circle cx="104" cy="122" r="1.6"/><circle cx="124" cy="122" r="1.6"/><circle cx="144" cy="122" r="1.6"/><circle cx="160" cy="122" r="1.6"/>
    <circle cx="4" cy="140" r="1.6"/><circle cx="24" cy="140" r="1.6"/><circle cx="44" cy="140" r="1.6"/><circle cx="64" cy="140" r="1.6"/><circle cx="84" cy="140" r="1.6"/><circle cx="104" cy="140" r="1.6"/><circle cx="124" cy="140" r="1.6"/><circle cx="144" cy="140" r="1.6"/><circle cx="160" cy="140" r="1.6"/>
  </g>
</svg>
<h2 class="abs section-title" style="left:664px;top:772px"><b>WHO</b> WE ARE</h2>
<div class="abs rule" style="left:664px;top:830px;width:140px"></div>
<p class="abs about-text">Perspiciatis unde omnis iste natus error sit voluptatem accusantium dolorekser eomque laudantium, totam rem aperiam, eaque ipsa quaeases aeab illo inventore veritatis etlksae quasi architecto beatae vitae dicta sunt explicabo. Nemo enimklase ipmsaeosam voluptatem quia voluptas sit aspernatur aut odit aut fugit, sed quia consequuntur magni dolores eos qui ratione voluptatem sequi nesciunt. Neque porro quisquam est, qui dolorem ipsu.</p>
<div class="abs btn" style="left:664px;top:1083px;width:171px">LEARN MORE <i><svg width="14" height="14" viewBox="0 0 14 14"><path d="M2 7h10M8 3l4 4-4 4" stroke="#00AB8E" stroke-width="1.8" fill="none"/></svg></i></div>

<!-- services -->
<section class="abs services">
  <h2 class="abs section-title" style="left:0;width:1200px;text-align:center;top:78px"><b>OUR</b> SERVICES</h2>
  <div class="abs rule" style="left:531px;top:136px;width:138px"></div>

  <div class="abs card" style="left:113px;top:175px"><div class="ph" role="img" aria-label="Photo of developers coding at computer screens" style="background:linear-gradient(135deg,#4b4f55,#8a8d91 60%,#c7c3bd)"></div><h3>WEB DEVELOPMENT</h3><p>Perspiciatis unde omnisite natus error sit voluptatem accusantium.</p><a>Learn More</a></div>
  <div class="abs card" style="left:446px;top:175px"><div class="ph" role="img" aria-label="Photo of a designer working on a website layout on a monitor" style="background:linear-gradient(135deg,#d8d6d2,#b9b6b1 55%,#eeece8)"></div><h3>WEB DESIGN</h3><p>Perspiciatis unde omnisite natus error sit voluptatem accusantium.</p><a>Learn More</a></div>
  <div class="abs card" style="left:777px;top:175px"><div class="ph" role="img" aria-label="Photo of a designer reviewing mobile app screens on a monitor" style="background:linear-gradient(135deg,#c9cfd4,#e4e7ea 50%,#9fb8c9)"></div><h3>MOBILE APP DEVELOPMENT</h3><p>Perspiciatis unde omnisite natus error sit voluptatem accusantium.</p><a>Learn More</a></div>

  <div class="abs card" style="left:113px;top:630px"><div class="ph" role="img" aria-label="Photo of a team discussing documents beside a computer" style="background:linear-gradient(135deg,#a68a72,#d9cdc2 55%,#8f8c8a)"></div><h3>ECOMMERCE DEVELOPMENT</h3><p>Perspiciatis unde omnisite natus error sit voluptatem accusantium.</p><a>Learn More</a></div>
  <div class="abs card" style="left:446px;top:630px"><div class="ph" role="img" aria-label="Photo of a designer working at a desk in a bright office" style="background:linear-gradient(135deg,#d5d3cf,#b3aea8 55%,#e9e6e1)"></div><h3>LOGO DESIGN</h3><p>Perspiciatis unde omnisite natus error sit voluptatem accusantium.</p><a>Learn More</a></div>
  <div class="abs card" style="left:777px;top:630px"><div class="ph" role="img" aria-label="Photo of two colleagues looking at a laptop together" style="background:linear-gradient(135deg,#cfd3d6,#8d97a1 55%,#e1e3e4)"></div><h3>WORDPRESS DEVELOPMENT</h3><p>Perspiciatis unde omnisite natus error sit voluptatem accusantium.</p><a>Learn More</a></div>
</section>

<!-- testimonials -->
<section class="abs testi">
  <h2 class="abs" style="left:0;width:1200px;text-align:center;top:82px;font-size:36px;font-weight:700;color:#fff;letter-spacing:.5px">TESTIMONIALS</h2>
  <div class="abs" style="left:489px;top:135px;width:48px;height:4px;background:#fff"></div>
  <div class="abs" style="left:537px;top:137px;width:89px;height:1.5px;background:#fff"></div>

  <div class="abs tcard" style="left:111px;top:169px">
    <p>Perspiciatis unde omnisiste natus error sitolup tatem accusantium doloremque laudantium, totam rem aperia meaque ipsaqu aeab illo inventore veritatis etquasi spiciatis unde omnisiste natus error sitolup tatem accusantium doloremque laudantium, totam rem aperia meaque ipsaqu aeab illoet quasi.</p>
    <div class="bar"></div>
    <div class="name">Dario Kestel</div>
    <div class="role">-Ceo, Orvanta</div>
    <svg class="abs" style="left:355px;top:178px" width="60" height="48" viewBox="0 0 60 48"><path d="M2 0h24v26l-10 20H6l6-18H2zM34 0h24v26l-10 20h-10l6-18h-10z" fill="#F7CA91" opacity=".45"/></svg>
    <svg class="abs" style="left:350px;top:254px" width="50" height="34" viewBox="0 0 50 34"><polygon points="0,0 50,0 50,34" fill="#fff"/></svg>
  </div>
  <div class="abs tcard" style="left:629px;top:169px">
    <p>Perspiciatis unde omnisiste natus error sitolup tatem accusantium doloremque laudantium, totam rem aperia meaque ipsaqu aeab illo inventore veritatis etquasi spiciatis unde omnisiste natus error sitolup tatem accusantium doloremque laudantium, totam rem aperia meaque ipsaqu aeab illoet quasi.</p>
    <div class="bar"></div>
    <div class="name">Dario Kestel</div>
    <div class="role">-Ceo, Orvanta</div>
    <svg class="abs" style="left:355px;top:178px" width="60" height="48" viewBox="0 0 60 48"><path d="M2 0h24v26l-10 20H6l6-18H2zM34 0h24v26l-10 20h-10l6-18h-10z" fill="#F7CA91" opacity=".45"/></svg>
    <svg class="abs" style="left:350px;top:254px" width="50" height="34" viewBox="0 0 50 34"><polygon points="0,0 50,0 50,34" fill="#fff"/></svg>
  </div>

  <div class="abs" style="left:540px;top:498px;width:34px;height:3px;background:var(--orange)"></div>
  <div class="abs" style="left:582px;top:498px;width:21px;height:3px;background:#fff"></div>
  <div class="abs" style="left:611px;top:498px;width:21px;height:3px;background:#fff"></div>
  <div class="abs" style="left:640px;top:498px;width:21px;height:3px;background:#fff"></div>
</section>

<!-- blog -->
<h2 class="abs section-title" style="left:0;width:1200px;text-align:center;top:3055px"><b>OUR</b> BLOG</h2>
<div class="abs rule" style="left:531px;top:3114px;width:138px"></div>

<div class="abs" style="left:111px;top:3145px;width:637px;height:473px;background:linear-gradient(135deg,#5b5f63,#a9a7a3 45%,#3f4347)" role="img" aria-label="Photo of a man with glasses thinking in front of a laptop under a pendant lamp"></div>
<article class="abs post" style="left:421px;top:3389px;width:317px;height:219px">
  <h4>Perspiciatis unde omnisiste natus error sit voluptatem accusantium dolore.</h4>
  <p>Jaispiciatis unde omnis iste natus error sit voluptatemaccusantium doloremquela udan tiumtotam rem aperiam, eaque ipsa quae ab</p>
  <a>Learn More <svg width="24" height="10" viewBox="0 0 24 10"><path d="M0 5h22M17 1l5 4-5 4" stroke="#F0912C" stroke-width="1.5" fill="none"/></svg></a>
</article>
<article class="abs post post-side" style="left:769px;top:3145px;height:225px">
  <h4>Perspiciatis unde omnisiste natus error sit voluptatem accusantium dolore.</h4>
  <p>Jaispiciatis unde omnis iste natus error sit voluptatemaccusantium doloremquela udan tiumtotam rem aperiam, eaque ipsa quae ab</p>
  <a>Learn More <svg width="24" height="10" viewBox="0 0 24 10"><path d="M0 5h22M17 1l5 4-5 4" stroke="#F0912C" stroke-width="1.5" fill="none"/></svg></a>
</article>
<article class="abs post post-side" style="left:769px;top:3389px;height:227px">
  <h4>Perspiciatis unde omnisiste natus error sit voluptatem accusantium dolore.</h4>
  <p>Jaispiciatis unde omnis iste natus error sit voluptatemaccusantium doloremquela udan tiumtotam rem aperiam, eaque ipsa quae ab</p>
  <a>Learn More <svg width="24" height="10" viewBox="0 0 24 10"><path d="M0 5h22M17 1l5 4-5 4" stroke="#F0912C" stroke-width="1.5" fill="none"/></svg></a>
</article>
<div class="abs btn" style="left:515px;top:3647px;width:170px">VIEW MORE <i><svg width="14" height="14" viewBox="0 0 14 14"><path d="M2 7h10M8 3l4 4-4 4" stroke="#00AB8E" stroke-width="1.8" fill="none"/></svg></i></div>

<!-- footer -->
<footer class="abs footer">
  <div class="abs logo" style="left:113px;top:148px;color:#fff">
    <div class="logo-name">QUENVADO</div>
    <div class="logo-sub">COMMUNICATIONS LTD</div>
  </div>
  <div class="abs fcol" style="left:330px;top:82px">
    <h5>QUICK LINKS</h5><div class="rule"></div>
    <ul><li>Home</li><li>Our Services</li><li>About Us</li><li>Portfolio</li><li>Team</li><li>Contact Us</li></ul>
  </div>
  <div class="abs fcol" style="left:518px;top:82px">
    <h5>LINKS</h5><div class="rule"></div>
    <ul><li>FAQ's</li><li>Terms &amp; Conditions</li><li>Privacy Policy</li><li>Site Map</li><li>Cookies Policy</li></ul>
  </div>
  <div class="abs fcol" style="left:708px;top:82px">
    <h5>SUPPORT</h5><div class="rule"></div>
    <ul><li>Copyright</li><li>Legal</li><li>Privacy</li><li>Accessibility</li><li>Sitemap</li></ul>
  </div>
  <div class="abs fcol" style="left:912px;top:82px">
    <h5>STAY CONNECTED</h5><div class="rule"></div>
  </div>
  <div class="abs social" style="left:915px;top:153px" aria-label="Social profile"></div>
  <div class="abs social" style="left:956px;top:153px" aria-label="Social profile"></div>
  <div class="abs social" style="left:996px;top:153px" aria-label="Social profile"></div>
  <div class="abs" style="left:111px;top:298px;width:978px;height:1px;background:#5a5a5a"></div>
  <div class="abs" style="left:0;width:1200px;text-align:center;top:317px;font-size:11.5px;font-weight:500">© COPYRIGHT 2022 | ALL RIGHTS RESERVED</div>
  <div class="abs" style="left:1117px;top:268px;width:44px;height:44px;border-radius:50%;background:var(--orange);display:flex;align-items:center;justify-content:center"><svg width="14" height="10" viewBox="0 0 14 10"><path d="M2 8l5-5 5 5" stroke="#fff" stroke-width="2" fill="none"/></svg></div>
</footer>

</body>
</html>
```